I want a business letter head designed, one that I can have printed but also one that I can use as an insert for proforma documentation that is printed in house.

Business name : RJ Pemberly & Associates
Address: PO Box 732
Coralbrook Qld 4871

Type of business: Accounting practice- accounting, taxation, audit, self managed superannuation,

Colour scheme: black and blue - previously designed a business card; however the blue that is one the cards is very washed out and I am not particularly happy with it.

```html
<!DOCTYPE html>
<html lang="en">
<head>
<meta charset="utf-8">
<title>RJ Pemberly &amp; Associates — Letterhead</title>
<link rel="stylesheet" href="https://fonts.googleapis.com/css2?family=Tinos:wght@400&display=swap">
<style>
  :root {
    --ink: #111111;
    --muted: #a3a3a3;
    --rule: #d9d9d9;
    --paper: #ffffff;
    --brand-blue: #cfe5f4;
  }
  html, body {
    margin: 0;
    padding: 0;
    width: 927px;
    height: 1200px;
    overflow: hidden;
    background: var(--paper);
  }
  .letterhead {
    position: relative;
    width: 927px;
    height: 1200px;
    background: var(--paper);
    font-family: "Tinos", "Times New Roman", serif;
    color: var(--ink);
    font-size: 15.6px;
    line-height: 20px;
  }
  .brand {
    position: absolute;
    top: 70px;
    left: 0;
    width: 927px;
    text-align: center;
  }
  .brand-name {
    display: inline-flex;
    align-items: center;
    gap: 10px;
    font-size: 27px;
    line-height: 34px;
    letter-spacing: 0.5px;
    color: var(--ink);
    margin: 0;
    font-weight: 400;
  }
  .brand-mark {
    width: 14px;
    height: 14px;
    background: var(--brand-blue);
    display: inline-block;
  }
  .brand-address {
    margin: 58px 0 0;
    font-style: normal;
    color: var(--muted);
    font-size: 14.5px;
    line-height: 17px;
  }
  .letter {
    position: absolute;
    left: 174px;
    top: 245px;
    width: 584px;
  }
  .recipient {
    margin: 0;
    font-style: normal;
  }
  .salutation { margin: 20px 0 0; }
  .letter-body p { margin: 20px 0 0; }
  .closing { margin: 20px 0 0; }
  .signatory { margin: 60px 0 0; }
  .footer-rule {
    position: absolute;
    left: 255px;
    top: 1135px;
    width: 418px;
    height: 1px;
    background: var(--rule);
    border: 0;
    margin: 0;
  }
</style>
</head>
<body>
<main class="letterhead">
  <header class="brand">
    <h1 class="brand-name"><span class="brand-mark" aria-hidden="true"></span>RJ Pemberly &amp; Associates</h1>
    <address class="brand-address">PO Box 732<br>Coralbrook Qld 4871</address>
  </header>

  <section class="letter">
    <address class="recipient">
      Lenii Grusx<br>
      Title<br>
      Company Name<br>
      4321 First Street<br>
      Anytown, State ZIP<br>
      Date 9/10/14
    </address>

    <p class="salutation">Dear Trenz,</p>

    <div class="letter-body">
      <p>Lorem ipsum dolor sit amet, consectetur adipiscing elit, set eiusmod tempor incidunt et labore et dolore magna aliquam. Ut enim ad minim veniam, quis nostrud exerc. Irure dolor in reprehend incididunt ut labore et dolore magna aliqua. Ut enim ad minim veniam, quis nostrud exercitation ullamco laboris nisi ut aliquip ex ea commodo consequat. Duis aute irure dolor in reprehenderit in voluptate velit esse molestaie cillum. Tia non ob ea soluad incom dereud facilis est er expedit distinct. Nam liber te conscient to factor tum poen legum odioque civiuda et tam. Neque pecun modut est neque nonor et imper ned libidig met, consectetur adipiscing elit, sed ut labore et dolore magna aliquam is nostrud exercitation ullam mmodo consequet. Duis aute in voluptate velit esse cillum dolore eu fugiat nulla pariatur.</p>

      <p>At vver eos et accusam dignissum qui blandit est praesent. Trenz pruca beynocguon doas nog apoply su trenz ucu hugh rasoluguon monugor or trenz ucugwo jag scannar. Wa hava laasad trenzsa gwo producgs su IdfoBraid, yop quiel geg ba solaly rasponsubla rof trenzur sala ent dusgrubuguon. Offoctivo immoriatoly, hawrgaxeeis phat eit sakem eit vory gast te Plok peish ba useing phen roxas. Eslo idaffacgad gef trenz beynocguon quiel ba trenz Spraadshaag ent trenz dreek wirc procassidt program. Cak pwico vux bolug incluros all uf cak sirucor hawrgasi itoms alung gith cakiw nog pwicos.</p>

      <p>Plloaso mako nuto uf cakso dodtos anr koop a cupy uf cak vux noaw yerw phuno. Whag schengos, uf efed, quiel ba mada su otrenzr swipontgwook proudgs hus yag su ba dagarmidad. Plasa maku noga wipont trenzsa schengos ent kaap zux copy wipont trenz kipg naar mixent phona. Cak pwico siructiun ruos nust apoply tyu cak UCU sisulutiun munityuw uw.</p>
    </div>

    <p class="closing">Sincerely yours,</p>
    <p class="signatory">Urna Semper</p>
  </section>

  <hr class="footer-rule">
</main>
</body>
</html>
```